Business Card For Kelmora Financial Consulting

Hi, I would like a business card designed. Bold, modern.
Please use the same design as the logo. I have also attached the website design to see the overall theme.
Wordmark Font
Color: Hex: #01AEF7

```html
<!DOCTYPE html>
<html lang="en">
<head>
<meta charset="utf-8">
<title>Kelmora Financial Consulting — Business Card</title>
<link href="https://fonts.googleapis.com/css2?family=Arimo:wght@400;700&display=swap" rel="stylesheet">
<style>
  :root {
    --page-bg: #1a1c1f;
    --card-bg: #0f1a22;
    --card-bg-edge: #132029;
    --accent: #01aef7;
    --text-light: #f2f4f6;
    --divider: #9aa3aa;
  }
  * { margin: 0; padding: 0; box-sizing: border-box; }
  html, body {
    width: 1200px; height: 963px; overflow: hidden;
    background: var(--page-bg);
    font-family: "Arimo", Arial, sans-serif;
  }
  .sheet {
    width: 1200px; height: 963px;
    display: flex; flex-direction: column;
    align-items: center; justify-content: center; gap: 40px;
  }
  .card {
    position: relative;
    width: 760px; height: 434px;
    border-radius: 34px;
    background: linear-gradient(160deg, var(--card-bg-edge), var(--card-bg) 60%);
    border-bottom: 5px solid var(--accent);
    overflow: hidden;
    box-shadow: 0 18px 40px rgba(0,0,0,.5);
  }
  /* front */
  .brand {
    position: absolute; left: 64px; top: 150px;
    display: flex; align-items: center; gap: 16px;
  }
  .brand-square {
    width: 48px; height: 48px; border: 4px solid var(--accent);
  }
  .brand-name {
    color: var(--text-light);
    font-weight: 700; font-size: 25px; line-height: 1.15;
    letter-spacing: 1px; text-transform: uppercase;
    width: 250px;
  }
  .divider {
    position: absolute; left: 400px; top: 92px;
    width: 1px; height: 250px; background: var(--divider);
  }
  .contact { position: absolute; left: 436px; top: 108px; color: var(--text-light); }
  .person-name {
    color: var(--accent); font-weight: 700; font-size: 27px;
    text-transform: uppercase; letter-spacing: .5px;
  }
  .person-role { font-size: 18px; margin-top: 4px; }
  .address { font-size: 18px; line-height: 1.35; margin-top: 22px; }
  .details { list-style: none; margin-top: 22px; font-size: 18px; }
  .details li { display: flex; align-items: center; gap: 12px; margin-bottom: 10px; }
  .details svg { width: 18px; height: 18px; fill: var(--accent); flex: none; }
  /* back */
  .back-brand {
    position: absolute; right: 60px; bottom: 56px;
    color: var(--text-light);
    font-weight: 700; font-size: 30px; letter-spacing: 1.5px;
    text-transform: uppercase; text-align: right; line-height: 1.2;
  }
</style>
</head>
<body>
<main class="sheet">
  <section class="card card-front">
    <div class="brand">
      <span class="brand-square"></span>
      <span class="brand-name">Kelmora Financial Consulting</span>
    </div>
    <span class="divider"></span>
    <div class="contact">
      <p class="person-name">Daniel Reyes</p>
      <p class="person-role">Manager</p>
      <p class="address">Your Address, City<br>State, Zip 0000</p>
      <ul class="details">
        <li>
          <svg viewBox="0 0 24 24"><path d="M6.6 10.8a15.1 15.1 0 0 0 6.6 6.6l2.2-2.2a1 1 0 0 1 1-.25 11.4 11.4 0 0 0 3.6.57 1 1 0 0 1 1 1V20a1 1 0 0 1-1 1A17 17 0 0 1 3 4a1 1 0 0 1 1-1h3.5a1 1 0 0 1 1 1c0 1.25.2 2.45.57 3.57a1 1 0 0 1-.25 1z"/></svg>
          555-214-7730
        </li>
        <li>
          <svg viewBox="0 0 24 24"><path d="M2 5h20v14H2z M2 5l10 8 10-8" fill="none" stroke="#01aef7" stroke-width="2"/></svg>
          daniel@kelmorafc.com
        </li>
        <li>
          <svg viewBox="0 0 24 24"><circle cx="12" cy="12" r="9" fill="none" stroke="#01aef7" stroke-width="2"/><path d="M3 12h18M12 3c3 3 3 15 0 18M12 3c-3 3-3 15 0 18" fill="none" stroke="#01aef7" stroke-width="1.6"/></svg>
          www.kelmorafc.com
        </li>
      </ul>
    </div>
  </section>

  <section class="card card-back">
    <p class="back-brand">Kelmora Financial<br>Consulting</p>
  </section>
</main>
</body>
</html>
```